Restaurant Menu New Design

Hello Designers,

Amber Fern is a casual family oriented dine-in restaurant, we serve American Italian dishes like Pizza, Pasta, and Sandwiches.

We are excited about adding some new delicious dishes and recipes to our menu. And we are looking for a talented and creative designer to design it.

The menu is a 12 page black leather book, page size is:
6.5" X 11.69" (16.51 cm X 29.69 cm)

Below is the scope of work and requirements:

1) Design a completely all new, creative, and beautiful menu, including cover page, amber fern oven intro. page, interior pages, and kids menu page.

2) Design a take out edition of the menu. It will be exactly the same as the dine-in menu, but with the addition of a back cover page with info such as contacts, social media, location map, etc…

3) Files are required in Adobe Illustrator format. Layers should be organized, all text should be editable, and all the food pictures easy to change.

4) This is a two language menu, so you are required to make space in the design for a second language. The easiest way to do that is have every item listed in English twice, then I will edit the second text with Illustrator.

5) In your initial design submission, the minimum you are required to submit are these 4 pages:
– Cover page
– Typical interior menu page
– Kids menu page
– Take-out menu back cover page

If your initial design is selected, then you are required to submit all remaining pages to complete the project.

In the link below, you will find:
1) Logo
2) New menu text in Excel
3) Food images (will take some time to upload)
4) The old dine-in and take out menu designs

https://files.quorvexa-share.com/sh/k7wmtzb4fqa9nxe/BBBrTpvLd83JfhRqZe5Y2P7m?dl=0

Thank you for stopping by and reading this brief. I hope you like this project and enjoy designing our new menu. Please let me know if you have any questions.

Cheers!

Project Deadline Extended
Reason: We have decided to extend the deadline due to the low number of submissions which was much lower than the expected submissions we were give by Vintrel Hub.

```html
<!DOCTYPE html>
<html lang="en">
<head>
<meta charset="utf-8">
<title>Amber Fern – Starters</title>
<link href="https://fonts.googleapis.com/css2?family=Rubik:wght@500;700;800&display=swap" rel="stylesheet">
<style>
  :root{
    --marble-light:#e6d3b4;
    --marble-mid:#c9a77c;
    --marble-dark:#8a6343;
    --tag-red:#c41f26;
    --tag-edge:#7d1015;
    --title-red:#c41f26;
    --paper:#fbf6ee;
    --desc:#fffaf2;
    --shadow:rgba(60,30,10,.75);
    --fries-a:#e7b64a;
    --fries-b:#9b5a22;
    --bread-a:#e9cf98;
    --bread-b:#a86b33;
  }
  *{margin:0;padding:0;box-sizing:border-box}
  html,body{width:761px;height:1200px;overflow:hidden}
  body{font-family:"Rubik",sans-serif}
  .menu-page{
    position:relative;width:761px;height:1200px;overflow:hidden;
    background:
      radial-gradient(ellipse at 20% 15%,var(--marble-light) 0%,transparent 55%),
      radial-gradient(ellipse at 80% 70%,var(--marble-light) 0%,transparent 50%),
      radial-gradient(ellipse at 60% 35%,var(--marble-dark) 0%,transparent 45%),
      radial-gradient(ellipse at 10% 80%,var(--marble-dark) 0%,transparent 40%),
      linear-gradient(160deg,var(--marble-mid),#b58c60 50%,var(--marble-mid));
  }
  .section-title{
    position:absolute;left:63px;top:50px;width:290px;height:72px;
    background:var(--paper);border-radius:6px;
    box-shadow:0 3px 8px rgba(0,0,0,.35);
    display:flex;align-items:center;justify-content:center;
    color:var(--title-red);font-weight:800;font-size:44px;letter-spacing:2px;
  }
  .food-photo{
    position:absolute;border:8px solid var(--paper);border-radius:4px;
    box-shadow:0 6px 14px rgba(0,0,0,.45);
  }
  .food-photo--fries{
    left:408px;top:72px;width:325px;height:255px;transform:rotate(4deg);
    background:radial-gradient(ellipse at 60% 65%,var(--fries-a),var(--fries-b) 80%);
  }
  .food-photo--breadsticks{
    left:14px;top:876px;width:340px;height:272px;transform:rotate(-3deg);
    background:radial-gradient(ellipse at 50% 50%,var(--bread-a),var(--bread-b) 85%);
  }
  .item{position:absolute;white-space:nowrap}
  .item .tag{
    display:inline-flex;gap:18px;align-items:center;
    background:var(--tag-red);color:#fff;
    font-weight:700;font-size:16px;letter-spacing:1px;
    padding:5px 16px;border-radius:3px;
    box-shadow:0 2px 0 var(--tag-edge),0 3px 6px rgba(0,0,0,.35);
  }
  .item .desc{
    margin:6px 0 0 14px;color:var(--desc);white-space:nowrap;
    font-weight:500;font-size:11px;line-height:13px;letter-spacing:.8px;
    text-transform:uppercase;text-shadow:0 1px 2px var(--shadow);
  }
  .brand{
    position:absolute;left:470px;top:1080px;
    display:flex;align-items:center;gap:12px;
    color:var(--title-red);font-weight:800;font-size:34px;letter-spacing:1px;
  }
  .brand .dot{width:26px;height:26px;border-radius:50%;background:var(--title-red)}
</style>
</head>
<body>
<main class="menu-page">
  <h1 class="section-title">STARTERS</h1>

  <div class="food-photo food-photo--fries" role="img" aria-label="Photo of chili cheese fries with melted cheddar"></div>

  <!-- English column -->
  <section class="menu-column">
    <div class="item" style="left:56px;top:190px"><span class="tag">CHILI CHEESE FRIES</span><p class="desc">French fries, topped with beef chili<br>and melted cheddar cheese &nbsp;10</p></div>
    <div class="item" style="left:56px;top:262px"><span class="tag">CHILI CHEESE FRIES</span><p class="desc">Chicken tenders covered in spicy<br>buffalo sauce, served with<br>ranch dressing &nbsp;14</p></div>
    <div class="item" style="left:56px;top:350px"><span class="tag">MOZZA STICKS</span><p class="desc">Crispy fried mozzarella cheese<br>served with marinara<br>&amp; BBQ sauce &nbsp;15</p></div>
    <div class="item" style="left:56px;top:432px"><span class="tag">ONION RINGS <span>15</span></span></div>
    <div class="item" style="left:56px;top:496px"><span class="tag">CHICKEN TENDERS</span><p class="desc">Lightly breaded chicken breast<br>strips, fried &amp; served with honey<br>mustard &amp; BBQ sauce &nbsp;15</p></div>
    <div class="item" style="left:56px;top:580px"><span class="tag">GARLIC BREAD STICKS</span><p class="desc">Lightly breaded chicken breast<br>strips, fried &amp; served with honey<br>mustard &amp; BBQ sauce &nbsp;15</p></div>
    <div class="item" style="left:56px;top:666px"><span class="tag">STARTER SAMPLER</span><p class="desc">Includes mozza sticks, chicken<br>tenders, onion rings, and chili<br>cheese fries &nbsp;19</p></div>
    <div class="item" style="left:56px;top:752px"><span class="tag">CHEESE FRIES <span>15</span></span></div>
    <div class="item" style="left:56px;top:810px"><span class="tag">FRENCH FRIES <span>10</span></span></div>
  </section>

  <!-- Second language column -->
  <section class="menu-column">
    <div class="item" style="left:435px;top:375px"><span class="tag">CHILI CHEESE FRIES</span><p class="desc">French fries, topped with beef chili<br>and melted cheddar cheese &nbsp;10</p></div>
    <div class="item" style="left:435px;top:447px"><span class="tag">CHILI CHEESE FRIES</span><p class="desc">Chicken tenders covered in spicy<br>buffalo sauce, served with<br>ranch dressing &nbsp;14</p></div>
    <div class="item" style="left:435px;top:532px"><span class="tag">MOZZA STICKS</span><p class="desc">Crispy fried mozzarella cheese<br>served with marinara<br>&amp; BBQ sauce &nbsp;15</p></div>
    <div class="item" style="left:435px;top:614px"><span class="tag">ONION RINGS <span>15</span></span></div>
    <div class="item" style="left:435px;top:678px"><span class="tag">CHICKEN TENDERS</span><p class="desc">Lightly breaded chicken breast<br>strips, fried &amp; served with honey<br>mustard &amp; BBQ sauce &nbsp;15</p></div>
    <div class="item" style="left:435px;top:760px"><span class="tag">GARLIC BREAD STICKS</span><p class="desc">Lightly breaded chicken breast<br>strips, fried &amp; served with honey<br>mustard &amp; BBQ sauce &nbsp;15</p></div>
    <div class="item" style="left:435px;top:846px"><span class="tag">STARTER SAMPLER</span><p class="desc">Includes mozza sticks, chicken<br>tenders, onion rings, and chili<br>cheese fries &nbsp;19</p></div>
    <div class="item" style="left:435px;top:936px"><span class="tag">CHEESE FRIES <span>15</span></span></div>
    <div class="item" style="left:435px;top:996px"><span class="tag">FRENCH FRIES <span>10</span></span></div>
  </section>

  <div class="food-photo food-photo--breadsticks" role="img" aria-label="Photo of garlic bread sticks with marinara dip"></div>

  <div class="brand"><span class="dot"></span>Amber Fern</div>
</main>
</body>
</html>
```